QRV Business Cards

We are looking for innovative edits to freshen up the card we uploaded. Several examples to choose from will be very helpful. Once we get this decided we will need cards for approximately 20 people.

From the BC attached you will see most of the content we want to keep, we are looking for layout options..the Logo must stay red/blue everything else may be changed to enhance.

Each employee will have their picture on the card.

Target Market(s)

B2B and Government agencies

Industry/Entity Type

Business

Contact Information for Business Card

This is a double sided fold over business card.

Requirements
Must have
• LOGO - same color and format
• LED Lighting Solutions w/Design, Installation, Financing as a stand out
Nice to have
• We had a cartoon charter drawn but I'm not sure if he will fit the card or not...just providing an idea.

```html
<!DOCTYPE html>
<html lang="en">
<head>
<meta charset="utf-8">
<title>QRV Business Cards</title>
<link href="https://fonts.googleapis.com/css2?family=Arimo:wght@400;700&display=swap" rel="stylesheet">
<style>
  :root {
    --bg: #e9e6e2;
    --sky-top: #5f98e3;
    --sky-bottom: #b9d6f6;
    --navy: #1b1f86;
    --red: #d8232a;
    --ink: #1a1a1a;
    --white: #ffffff;
    --shadow: rgba(0,0,0,0.22);
  }
  * { box-sizing: border-box; margin: 0; padding: 0; }
  html, body { width: 1200px; height: 960px; overflow: hidden; }
  body {
    background: var(--bg);
    font-family: "Arimo", Arial, sans-serif;
    color: var(--ink);
    position: relative;
  }
  .card {
    position: absolute;
    left: 250px;
    width: 700px;
    height: 400px;
    box-shadow: 0 6px 18px var(--shadow);
    overflow: hidden;
  }
  /* Back of card */
  .card-back {
    top: 40px;
    background: linear-gradient(160deg, var(--sky-top) 0%, var(--sky-bottom) 100%);
  }
  .mascot {
    position: absolute;
    right: 50px;
    top: 18px;
    width: 180px;
    height: 130px;
    border-radius: 12px;
    background: linear-gradient(180deg, #3b5fc7 0%, #d8232a 100%);
    opacity: 0.85;
  }
  .contact-lines {
    position: absolute;
    left: 48px;
    top: 120px;
    list-style: none;
  }
  .contact-lines li {
    display: flex;
    align-items: center;
    gap: 12px;
    font-size: 18px;
    line-height: 28px;
  }
  .contact-lines svg { width: 16px; height: 16px; flex: none; }
  .services {
    position: absolute;
    list-style: none;
    font-size: 17px;
    line-height: 21px;
  }
  .services-left { left: 48px; top: 228px; }
  .services-right { left: 340px; top: 162px; }
  .led-callout {
    position: absolute;
    left: 340px;
    top: 326px;
    width: 320px;
    font-size: 15px;
    line-height: 20px;
    color: var(--navy);
  }
  .led-callout strong { color: var(--red); font-weight: 700; }
  /* Front of card */
  .card-front {
    top: 520px;
    background: var(--white);
    display: flex;
  }
  .brand-side {
    width: 390px;
    padding: 70px 40px 0 50px;
  }
  .brand-name {
    font-size: 110px;
    font-weight: 700;
    color: var(--red);
    letter-spacing: 4px;
    line-height: 1;
  }
  .tagline {
    margin-top: 70px;
    font-size: 22px;
    font-weight: 400;
    color: var(--navy);
    letter-spacing: 1px;
    line-height: 28px;
  }
  .tagline .accent { color: var(--red); }
  .profile-side {
    width: 290px;
    margin: 18px 20px 18px 0;
    background: var(--navy);
    color: var(--white);
    padding: 26px 22px;
    text-align: center;
  }
  .person-name { font-size: 26px; font-weight: 400; letter-spacing: 1px; }
  .person-title { font-size: 13px; margin-top: 4px; }
  .portrait {
    width: 150px;
    height: 130px;
    margin: 16px auto;
    border: 4px solid var(--white);
    background: linear-gradient(180deg, #b8a89a 0%, #3a2e2a 100%);
  }
  .details { font-size: 15px; line-height: 21px; }
  .details .web { font-size: 14px; margin-top: 6px; }
</style>
</head>
<body>
  <section class="card card-back">
    <div class="mascot" role="img" aria-label="Cartoon superhero company mascot in blue and red"></div>
    <ul class="contact-lines">
      <li><svg viewBox="0 0 16 16"><path d="M3 1l3 3-2 2c1 2 3 4 5 5l2-2 3 3-2 3C7 15 1 9 1 3z" fill="#d8232a"/></svg>800-555-0142</li>
      <li><svg viewBox="0 0 16 16"><rect x="4" y="1" width="8" height="14" rx="1.5" fill="none" stroke="#d8232a" stroke-width="2"/></svg>410-555-0187</li>
      <li><svg viewBox="0 0 16 16"><rect x="1" y="6" width="14" height="7" rx="1" fill="#d8232a"/><rect x="4" y="2" width="8" height="5" fill="#d8232a"/></svg>800-555-0143</li>
    </ul>
    <ul class="services services-left">
      <li>Roadway Lighting</li>
      <li>Sign Services</li>
      <li>Sports Lighting</li>
      <li>Stray Voltage Testing</li>
      <li>Traffic Signals</li>
      <li>Utility Locating</li>
      <li>Vacuum Excavation</li>
    </ul>
    <ul class="services services-right">
      <li>24 Emergency Service</li>
      <li>Directional Drilling</li>
      <li>Electrical Services</li>
      <li>Energy Audits</li>
      <li>Night Inspections</li>
      <li>Parking Lot Lighting</li>
      <li>Pole Inspections</li>
    </ul>
    <p class="led-callout"><strong>LED Lighting Solutions</strong><br>Design · Installation · Financing</p>
  </section>

  <section class="card card-front">
    <div class="brand-side">
      <div class="brand-name">QRV</div>
      <p class="tagline">THE LEADER IN<br><span class="accent">LIGHTING</span> SERVICES</p>
    </div>
    <div class="profile-side">
      <h1 class="person-name">Daniel Hargrove</h1>
      <p class="person-title">Chief Executive Officer</p>
      <div class="portrait" role="img" aria-label="Employee portrait photograph"></div>
      <div class="details">
        <p>415 Harbor Ave., Millbrook</p>
        <p>MD 20999</p>
        <p>DHargrove@qrvlighting.com</p>
        <p class="web">www.qrvlighting.com</p>
      </div>
    </div>
  </section>
</body>
</html>
```